Varlow Industries Luxury Candles

Luxury box design,, simple and sophisticated look,,

My collection of candles come in 5 different fragrances, i would like to be able to change the fragrance name on the boxes,,,,

I would like the outline of australia on the front down the bottom , (only small) to represent this is an australian product.

My boxes are white gloss,,,

Happy for you to use my current logo ,,, however you'll have to change Varlow Nails to Varlow Industries.

```html
<!DOCTYPE html>
<html lang="en">
<head>
<meta charset="utf-8">
<title>Varlow Industries – Coconut Lime Candle Box</title>
<link href="https://fonts.googleapis.com/css2?family=Oswald:wght@400&display=swap" rel="stylesheet">
<style>
  :root {
    --canvas-bg: #d8dcdf;
    --box-white: #f8f7f5;
    --marble-cream: #f1e6d3;
    --marble-warm: #ead2a8;
    --band-charcoal: #3e4546;
    --gold-line: #d8a93c;
    --gold-light: #e9c46a;
    --gold-dark: #b9832a;
    --label-ink: #3a2a12;
    --weight-ink: #4a3a20;
    --title-ink: #ffffff;
  }
  html, body {
    margin: 0;
    padding: 0;
    width: 1200px;
    height: 1025px;
    overflow: hidden;
    background: var(--canvas-bg);
  }
  .canvas {
    position: relative;
    width: 1200px;
    height: 1025px;
  }
  .box-front {
    position: absolute;
    left: 307px;
    top: 62px;
    width: 585px;
    height: 900px;
    background: var(--box-white);
    overflow: hidden;
    box-shadow: 0 8px 24px rgba(0,0,0,0.10);
  }
  .marble-surface {
    position: absolute;
    inset: 0;
    background: linear-gradient(155deg,
      var(--marble-cream) 0%,
      var(--box-white) 18%,
      var(--box-white) 40%,
      var(--marble-cream) 58%,
      var(--marble-warm) 70%,
      var(--marble-cream) 82%,
      var(--box-white) 100%);
  }
  .fragrance-band {
    position: absolute;
    left: 0;
    top: 296px;
    width: 100%;
    height: 105px;
    background: var(--band-charcoal);
  }
  .gold-frame {
    position: absolute;
    left: 67px;
    top: 252px;
    width: 451px;
    height: 192px;
    box-sizing: border-box;
    border: 2px solid var(--gold-line);
  }
  .brand-label {
    position: absolute;
    left: 176px;
    top: 223px;
    width: 233px;
    height: 59px;
    background: linear-gradient(100deg, var(--gold-dark), var(--gold-light) 45%, var(--gold-dark));
    display: flex;
    align-items: center;
    justify-content: center;
  }
  .brand-name {
    font-family: 'Oswald', sans-serif;
    font-weight: 400;
    font-size: 21px;
    letter-spacing: 1px;
    color: var(--label-ink);
  }
  .fragrance-name {
    position: absolute;
    left: 0;
    top: 296px;
    width: 100%;
    height: 105px;
    margin: 0;
    display: flex;
    align-items: center;
    justify-content: center;
    font-family: 'Oswald', sans-serif;
    font-weight: 400;
    font-size: 32px;
    letter-spacing: 15px;
    padding-left: 15px;
    box-sizing: border-box;
    color: var(--title-ink);
  }
  .net-weight {
    position: absolute;
    left: 0;
    top: 414px;
    width: 100%;
    margin: 0;
    line-height: 18px;
    text-align: center;
    font-family: 'Oswald', sans-serif;
    font-weight: 400;
    font-size: 15px;
    color: var(--weight-ink);
  }
</style>
</head>
<body>
  <main class="canvas">
    <section class="box-front">
      <div class="marble-surface" role="img" aria-label="White marble texture with gold veining"></div>
      <div class="fragrance-band"></div>
      <div class="gold-frame"></div>
      <div class="brand-label"><span class="brand-name">Varlow Industries</span></div>
      <h1 class="fragrance-name">COCONUT LIME</h1>
      <p class="net-weight">350g</p>
    </section>
  </main>
</body>
</html>
```